TalkWell Needs a Business Card

We need a business card for Tomas Ferreby, Ph.D., CCC-SLP, who is affiliated with Hollander Ridge University. He is an Associate Professor and Licensed Speech-Language Pathologist, Department of Communication Disorders, College of Health and Human Services.

He has a consulting business "TalkWell Consultant". The logo is attached. The consulting company color is Turquoise. HRU school color is orange.

The consulting business focus on: Consultation, Research & Professional Development. Our target market is individuals with annual family income of $100,000.00 or more for consultation and speech-language pathologists for professional development activities.

No harsh colors, subtle colors appreciated. Address, e-mail, telephone, and small scan logo for a link to our website. Creativity in design will be appreciated. Please add your comments, why you created this design?

Thanks and looking for submissions.

```html
<!DOCTYPE html>
<html lang="en">
<head>
<meta charset="utf-8">
<title>TalkWell Consultants – Business Card</title>
<link rel="stylesheet" href="https://fonts.googleapis.com/css2?family=Open+Sans:wght@400;600&display=swap">
<style>
  :root {
    --page: #e6e6e7;
    --charcoal: #474749;
    --turquoise: #49c4c8;
    --green: #3aaa35;
    --ink: #1f2a2c;
    --white: #ffffff;
  }
  * { box-sizing: border-box; margin: 0; padding: 0; }
  html, body {
    width: 1200px; height: 1200px; overflow: hidden;
    background: var(--page);
    font-family: "Open Sans", Arial, sans-serif;
  }
  .sheet {
    width: 1200px; height: 1200px;
    display: flex; flex-direction: column; align-items: center; justify-content: center;
    gap: 70px;
  }
  .card {
    position: relative; width: 700px; height: 400px; overflow: hidden;
    box-shadow: 0 8px 24px rgba(0,0,0,.18);
  }

  /* Front */
  .card--front { background: var(--charcoal); }
  .front-brand {
    position: absolute; left: 150px; top: 150px;
    display: flex; align-items: center; gap: 22px;
  }
  .brand-dot { width: 64px; height: 64px; border-radius: 50%; background: var(--turquoise); }
  .brand-name {
    display: block; font-size: 56px; font-weight: 400; line-height: 1; color: var(--turquoise);
  }
  .brand-sub {
    display: block; margin-top: 6px; font-size: 17px; letter-spacing: 6px;
    color: var(--green); text-align: right;
  }

  /* Back */
  .card--back { background: var(--turquoise); }
  .back-tab {
    position: absolute; left: 0; top: 58px; width: 34px; height: 40px; background: var(--green);
  }
  .back-brand { position: absolute; left: 56px; top: 52px; color: var(--white); }
  .back-brand .brand-name { color: var(--white); font-size: 34px; }
  .back-brand .brand-sub { color: var(--white); font-size: 10px; letter-spacing: 3px; margin-top: 3px; }
  .name-band {
    position: absolute; left: 290px; right: 0; top: 118px; height: 44px;
    background: var(--green); display: flex; align-items: center; padding-left: 20px;
  }
  .person-name { font-size: 20px; font-weight: 600; color: var(--ink); white-space: nowrap; }
  .person-role {
    position: absolute; left: 300px; top: 172px; width: 390px;
    font-size: 14px; line-height: 21px; color: var(--ink);
  }
  .contact-list {
    position: absolute; left: 300px; top: 252px; list-style: none;
    font-size: 14px; color: var(--ink);
  }
  .contact-list li { display: flex; align-items: center; gap: 10px; height: 28px; }
  .contact-icon { width: 18px; height: 18px; flex: none; }
</style>
</head>
<body>
<main class="sheet">
  <section class="card card--front" aria-label="Card front">
    <div class="front-brand">
      <span class="brand-dot"></span>
      <div>
        <span class="brand-name">TalkWell</span>
        <span class="brand-sub">CONSULTANTS</span>
      </div>
    </div>
  </section>

  <section class="card card--back" aria-label="Card back">
    <div class="back-tab"></div>
    <div class="back-brand">
      <span class="brand-name">TalkWell</span>
      <span class="brand-sub">CONSULTANTS</span>
    </div>
    <div class="name-band"><span class="person-name">Tomas Ferreby, Ph.D., CCC-SLP</span></div>
    <p class="person-role">
      Associate Professor &amp; Licensed SLP<br>
      Hollander Ridge University<br>
      1 University Pkwy, Harlow, IL 60466
    </p>
    <ul class="contact-list">
      <li>
        <svg class="contact-icon" viewBox="0 0 18 18" aria-hidden="true">
          <rect width="18" height="18" rx="4" fill="#3aaa35"/>
          <path d="M5 4h2.5l1 3-1.5 1a6 6 0 0 0 3 3l1-1.5 3 1V13a1.5 1.5 0 0 1-1.5 1.5A9 9 0 0 1 3.5 5.5 1.5 1.5 0 0 1 5 4z" fill="#fff"/>
        </svg>
        555 01 48 27
      </li>
      <li>
        <svg class="contact-icon" viewBox="0 0 18 18" aria-hidden="true">
          <rect width="18" height="18" rx="4" fill="#3aaa35"/>
          <rect x="3.5" y="5" width="11" height="8" rx="1" fill="none" stroke="#fff" stroke-width="1.4"/>
          <path d="M3.5 5.5 9 10l5.5-4.5" fill="none" stroke="#fff" stroke-width="1.4"/>
        </svg>
        tferreby@talkwellconsult.com
      </li>
      <li>
        <svg class="contact-icon" viewBox="0 0 18 18" aria-hidden="true">
          <rect width="18" height="18" rx="4" fill="#3aaa35"/>
          <circle cx="9" cy="9" r="5" fill="none" stroke="#fff" stroke-width="1.4"/>
          <path d="M4 9h10M9 4c-2.5 3-2.5 7 0 10M9 4c2.5 3 2.5 7 0 10" fill="none" stroke="#fff" stroke-width="1.1"/>
        </svg>
        www.talkwellconsult.com
      </li>
    </ul>
  </section>
</main>
</body>
</html>
```